Postcard Design - Simple

Freight Factoring Company - We purchase freight invoices from trucking companies. We then pay them the same day so they don't have to wait 4-6 weeks to get their money.

Industry/Entity Type

It Company

```html
<!DOCTYPE html>
<html lang="en">
<head>
<meta charset="utf-8">
<title>Haulway Capital – Postcard</title>
<link rel="stylesheet" href="https://fonts.googleapis.com/css2?family=Fira+Sans+Condensed:wght@400;500;600;700&family=Bebas+Neue&family=Arimo:wght@400;700&display=swap">
<style>
  :root {
    --navy: #0f2a5c;
    --navy-deep: #0a1f47;
    --royal: #1f4c9a;
    --royal-light: #3568bd;
    --ink: #1b1b1b;
    --panel-light: #ffffff;
    --panel-grey: #dfe2e6;
    --page: #ededed;
    --line: #b9bcc0;
    --white: #ffffff;
  }
  * { box-sizing: border-box; margin: 0; padding: 0; }
  html, body { width: 936px; height: 1200px; overflow: hidden; }
  body { background: var(--page); position: relative; font-family: "Fira Sans Condensed", "Arial Narrow", sans-serif; }

  .postcard {
    position: absolute;
    background: var(--panel-light);
    box-shadow: 0 6px 18px rgba(0,0,0,0.22);
    overflow: hidden;
  }
  .postcard-front { left: 112px; top: 51px; width: 666px; height: 516px; }
  .postcard-back  { left: 169px; top: 594px; width: 664px; height: 514px; }
  .shapes { position: absolute; inset: 0; }

  /* Front */
  .front-headline {
    position: absolute; left: 19px; top: 22px;
    color: var(--navy); font-weight: 600; font-size: 20px; line-height: 24px;
  }
  .steps { position: absolute; left: 19px; top: 115px; list-style: none; }
  .steps li {
    display: flex; align-items: flex-start; gap: 7px;
    color: var(--ink); font-size: 15px; font-weight: 500; line-height: 16px; margin-bottom: 8px;
  }
  .steps svg { flex: none; margin-top: 2px; }
  .brand-name {
    position: absolute; left: 40px; top: 230px; width: 250px; height: 70px;
    display: flex; align-items: center; gap: 10px;
    color: var(--white); font-weight: 600; font-size: 24px; letter-spacing: 1px; text-transform: uppercase;
  }
  .brand-mark { width: 14px; height: 14px; border-radius: 50%; background: var(--white); flex: none; }
  .simple-note { position: absolute; left: 19px; top: 340px; color: var(--royal); font-size: 15px; font-weight: 600; line-height: 25px; }
  .simple-note .services { color: var(--ink); font-weight: 500; }
  .cashflow-title {
    position: absolute; right: 30px; top: 448px;
    font-family: "Bebas Neue", "Impact", sans-serif; font-size: 46px; color: var(--white); letter-spacing: 0.5px;
  }

  /* Back */
  .details-tab {
    position: absolute; left: 0; top: 24px; width: 270px; height: 38px;
    background: var(--navy); border-radius: 0 14px 14px 0;
    color: var(--white); font-weight: 600; font-size: 19px; line-height: 38px; padding-left: 32px;
  }
  .details-list { position: absolute; left: 32px; top: 98px; list-style: none; }
  .details-list li {
    display: flex; align-items: center; gap: 7px;
    color: var(--ink); font-weight: 600; font-size: 16.5px; line-height: 28px;
  }
  .contact { position: absolute; left: 0; top: 356px; width: 384px; text-align: center; color: var(--white); font-family: "Arimo", Arial, sans-serif; }
  .contact-lead { font-size: 17px; font-weight: 700; }
  .contact-phone { font-size: 22px; font-weight: 700; margin-top: 4px; display: flex; justify-content: center; align-items: center; gap: 8px; }
  .contact-web { font-size: 17px; font-weight: 700; margin-top: 18px; }
  .contact-tag { font-size: 13px; margin-top: 3px; }
  .stamp-box { position: absolute; left: 558px; top: 24px; width: 90px; height: 62px; border: 1.5px solid var(--line); }
  .address-line { position: absolute; left: 396px; width: 254px; height: 1.5px; background: var(--line); }
</style>
</head>
<body>

<section class="postcard postcard-front">
  <svg class="shapes" viewBox="0 0 666 516" width="666" height="516" aria-hidden="true">
    <defs>
      <linearGradient id="frontBg" x1="0" y1="0" x2="1" y2="1">
        <stop offset="0" stop-color="#ffffff"/>
        <stop offset="1" stop-color="#d8dbe0"/>
      </linearGradient>
      <linearGradient id="band" x1="0" y1="0" x2="1" y2="0">
        <stop offset="0" stop-color="#1b3f86"/>
        <stop offset="1" stop-color="#3568bd"/>
      </linearGradient>
      <linearGradient id="navyFill" x1="0" y1="0" x2="1" y2="1">
        <stop offset="0" stop-color="#0a1f47"/>
        <stop offset="1" stop-color="#1a3f80"/>
      </linearGradient>
    </defs>
    <rect width="666" height="516" fill="url(#frontBg)"/>
    <rect x="0" y="222" width="360" height="83" fill="url(#band)"/>
    <path d="M0,450 C90,470 170,440 250,400 C330,362 430,360 520,368 C590,374 640,350 666,330 V516 H0 Z" fill="#f4f5f7" opacity="0.9"/>
    <path d="M0,472 C100,490 180,455 260,418 C340,382 440,380 530,388 C600,394 645,372 666,352 V516 H0 Z" fill="url(#navyFill)"/>
  </svg>

  <svg class="shapes" viewBox="0 0 666 516" width="666" height="516" role="img" aria-label="Photo of a forklift loading a giant roll of dollar bills into a white semi-trailer">
    <defs>
      <linearGradient id="photoTone" x1="0" y1="0" x2="1" y2="1">
        <stop offset="0" stop-color="#c9ccd0"/>
        <stop offset="0.5" stop-color="#9ea3a8"/>
        <stop offset="1" stop-color="#5f6469"/>
      </linearGradient>
    </defs>
    <path d="M300,0 H666 V352 C640,372 600,394 530,388 C480,384 440,382 410,386 C395,250 375,130 300,0 Z" fill="url(#photoTone)"/>
    <path d="M288,0 C365,130 386,250 400,390" fill="none" stroke="var(--royal)" stroke-width="5"/>
  </svg>

  <h1 class="front-headline">We buy freight invoices<br>and pay you the SAME DAY.<br>Here's how it works . .</h1>
  <ul class="steps">
    <li><svg width="12" height="12" viewBox="0 0 12 12"><rect x="0.75" y="0.75" width="10.5" height="10.5" fill="none" stroke="#333" stroke-width="1.5"/><path d="M3 6 L5.2 8.2 L11 2" fill="none" stroke="#333" stroke-width="1.6"/></svg>You Deliver the Load</li>
    <li><svg width="12" height="12" viewBox="0 0 12 12"><rect x="0.75" y="0.75" width="10.5" height="10.5" fill="none" stroke="#333" stroke-width="1.5"/><path d="M3 6 L5.2 8.2 L11 2" fill="none" stroke="#333" stroke-width="1.6"/></svg>You Send in Load Paperwork</li>
    <li><svg width="12" height="12" viewBox="0 0 12 12"><rect x="0.75" y="0.75" width="10.5" height="10.5" fill="none" stroke="#333" stroke-width="1.5"/><path d="M3 6 L5.2 8.2 L11 2" fill="none" stroke="#333" stroke-width="1.6"/></svg><span>We Send Your Cash via Direct<br>Deposit on the Same Day</span></li>
  </ul>
  <div class="brand-name"><span class="brand-mark"></span>Haulway Capital</div>
  <p class="simple-note">It's that simple!<br>We do the rest . . .<br><span class="services">Credit Checks, Invoicing, Collections, etc.</span></p>
  <h2 class="cashflow-title">Speed Up Cash Flow !</h2>
</section>

<section class="postcard postcard-back">
  <svg class="shapes" viewBox="0 0 664 514" width="664" height="514" aria-hidden="true">
    <defs>
      <linearGradient id="panelGrey" x1="0" y1="0" x2="1" y2="0">
        <stop offset="0" stop-color="#ffffff"/>
        <stop offset="1" stop-color="#d3d6db"/>
      </linearGradient>
      <linearGradient id="backNavy" x1="0" y1="0" x2="1" y2="1">
        <stop offset="0" stop-color="#0a1f47"/>
        <stop offset="1" stop-color="#1f4c9a"/>
      </linearGradient>
      <clipPath id="panelClip">
        <path d="M0,0 H296 C322,120 360,260 372,350 C380,420 365,480 340,514 H0 Z"/>
      </clipPath>
    </defs>
    <path d="M300,0 C332,120 378,260 388,350 C396,425 378,480 354,514 H338 C362,480 378,420 370,350 C358,260 320,120 290,0 Z" fill="var(--royal)"/>
    <g clip-path="url(#panelClip)">
      <rect width="400" height="514" fill="url(#panelGrey)"/>
      <rect y="338" width="400" height="176" fill="url(#backNavy)"/>
    </g>
  </svg>

  <div class="details-tab">HERE ARE THE DETAILS</div>
  <ul class="details-list">
    <li><svg width="12" height="12" viewBox="0 0 12 12"><circle cx="6" cy="6" r="5.2" fill="none" stroke="#333" stroke-width="1.3"/><path d="M5 3.5 L7.5 6 L5 8.5" fill="none" stroke="#333" stroke-width="1.5"/></svg>Short term contract</li>
    <li><svg width="12" height="12" viewBox="0 0 12 12"><circle cx="6" cy="6" r="5.2" fill="none" stroke="#333" stroke-width="1.3"/><path d="M5 3.5 L7.5 6 L5 8.5" fill="none" stroke="#333" stroke-width="1.5"/></svg>No Setup Fees</li>
    <li><svg width="12" height="12" viewBox="0 0 12 12"><circle cx="6" cy="6" r="5.2" fill="none" stroke="#333" stroke-width="1.3"/><path d="M5 3.5 L7.5 6 L5 8.5" fill="none" stroke="#333" stroke-width="1.5"/></svg>No Minimums</li>
    <li><svg width="12" height="12" viewBox="0 0 12 12"><circle cx="6" cy="6" r="5.2" fill="none" stroke="#333" stroke-width="1.3"/><path d="M5 3.5 L7.5 6 L5 8.5" fill="none" stroke="#333" stroke-width="1.5"/></svg>Online 24 Hour Account Access</li>
    <li><svg width="12" height="12" viewBox="0 0 12 12"><circle cx="6" cy="6" r="5.2" fill="none" stroke="#333" stroke-width="1.3"/><path d="M5 3.5 L7.5 6 L5 8.5" fill="none" stroke="#333" stroke-width="1.5"/></svg>Free Credit Checks</li>
    <li><svg width="12" height="12" viewBox="0 0 12 12"><circle cx="6" cy="6" r="5.2" fill="none" stroke="#333" stroke-width="1.3"/><path d="M5 3.5 L7.5 6 L5 8.5" fill="none" stroke="#333" stroke-width="1.5"/></svg>Fuel Cards Available (Save 10 ¢/gallon)</li>
    <li><svg width="12" height="12" viewBox="0 0 12 12"><circle cx="6" cy="6" r="5.2" fill="none" stroke="#333" stroke-width="1.3"/><path d="M5 3.5 L7.5 6 L5 8.5" fill="none" stroke="#333" stroke-width="1.5"/></svg>Easy &amp; Quick Qualification</li>
    <li><svg width="12" height="12" viewBox="0 0 12 12"><circle cx="6" cy="6" r="5.2" fill="none" stroke="#333" stroke-width="1.3"/><path d="M5 3.5 L7.5 6 L5 8.5" fill="none" stroke="#333" stroke-width="1.5"/></svg>We specialize in small fleets</li>
  </ul>

  <div class="contact">
    <p class="contact-lead">Contact Us Today</p>
    <p class="contact-phone">
      <svg width="18" height="18" viewBox="0 0 24 24" aria-hidden="true"><path d="M6.6 10.8c1.4 2.8 3.8 5.1 6.6 6.6l2.2-2.2c.3-.3.7-.4 1-.2 1.1.4 2.3.6 3.6.6.6 0 1 .4 1 1V20c0 .6-.4 1-1 1C10.6 21 3 13.4 3 4c0-.6.4-1 1-1h3.5c.6 0 1 .4 1 1 0 1.3.2 2.5.6 3.6.1.3 0 .7-.2 1L6.6 10.8z" fill="#ffffff"/></svg>
      555-014-2290
    </p>
    <p class="contact-web">www.haulwaycapital.com</p>
    <p class="contact-tag">(Carrier Solutions then Cash Flow Solutions)</p>
  </div>

  <div class="stamp-box"></div>
  <div class="address-line" style="top:178px"></div>
  <div class="address-line" style="top:221px"></div>
  <div class="address-line" style="top:264px"></div>
  <div class="address-line" style="top:306px"></div>
</section>

</body>
</html>
```